Pine Ember Coffee Needs A New Bag Label

We require a redesign of our coffee bag label. Our company, Pine Ember Coffee roasts and packages Fair Trade Organic Coffee in 5 lb and 1 lb bags hot from the roaster. Our company aligns itself with a Canadian outdoor lifestyle involving hiking, camping, canoeing, mountain biking etc. I am attaching our existing logo which is based on a "tent sign" used to indicate a campsite. I'm also attaching our company logo, which is based on a "Camp Patch" that is common for summer camps. The label needs to have "blank space" where I can change the name and description of the different coffees/blends. We use black coffee bags. We are looking for a label that is more upscale from what we currently have.
Target Market(s)
People who love coffee and enjoy outdoor activities. Camping, hiking, climbing, canoeing, sailing etc.
Industry/Entity Type
Coffee Shop
Requirements
Must have
- Project must have an editable space where we can change the name of the coffee (ie Nicaragua, Guatemala, French Roast) and a space where we can edit the descriptions (ie : Dark Roast, Full Body, Citrus Aroma etc)
- I am including a sample of our existing label. The triangle symbol is based on a symbol used to make a camp site. I am also including our logo which is based on a camp patch common at many summer camps in North America.
- The label must be 3" wide by 4" high
Should not have
- Must not be too busy.

```html
<!DOCTYPE html>
<html lang="en">
<head>
<meta charset="UTF-8">
<title>Pine Ember Coffee – Bag Label</title>
<link href="https://fonts.googleapis.com/css2?family=Oswald:wght@400;500;700&family=Playfair+Display+SC:wght@400&display=swap" rel="stylesheet">
<style>
  :root {
    --canvas: #eeeeec;
    --ember: #e8671c;
    --forest: #1f3d42;
    --paper: #ffffff;
    --bean-light: #e6e6e4;
    --bean-dark: #c9c9c7;
    --ink: #2a2a2a;
  }
  * { margin: 0; padding: 0; box-sizing: border-box; }
  html, body {
    width: 1200px; height: 877px; overflow: hidden;
    background: var(--canvas);
  }
  .label-set {
    position: relative; width: 1200px; height: 877px;
    display: flex; justify-content: center; align-items: center; gap: 60px;
  }
  .label {
    position: relative; width: 420px; height: 560px; overflow: hidden;
    font-family: "Oswald", sans-serif;
    box-shadow: 0 2px 10px rgba(0,0,0,0.12);
  }
  .label--light { background: var(--paper); }
  .label--dark { background: var(--forest); }

  .brand {
    position: absolute; top: 44px; left: 0; width: 100%;
    display: flex; justify-content: center; align-items: center; gap: 10px;
  }
  .brand__dot { width: 18px; height: 18px; border-radius: 50%; background: var(--ember); }
  .brand__name {
    font-weight: 500; font-size: 22px; letter-spacing: 1px; text-transform: uppercase;
  }
  .label--light .brand__name { color: var(--forest); }
  .label--dark .brand__name { color: var(--paper); }

  .treeline {
    position: absolute; top: 150px; left: 0; width: 100%; height: 72px;
  }
  .label--light .treeline { background: linear-gradient(to bottom, rgba(31,61,66,0) 0%, rgba(31,61,66,0.85) 55%, var(--forest) 100%); }
  .label--dark .treeline { background: linear-gradient(to bottom, rgba(255,255,255,0) 0%, rgba(255,255,255,0.85) 55%, var(--paper) 100%); }

  .blend-band {
    position: absolute; top: 222px; left: 0; width: 100%; height: 170px;
    background: var(--ember);
    padding: 14px 26px 0;
    text-transform: uppercase; line-height: 0.98;
  }
  .blend-band__origin { color: var(--paper); font-weight: 500; font-size: 30px; }
  .blend-band__headline { color: var(--forest); font-weight: 700; font-size: 60px; }
  .blend-band__sub { color: var(--paper); font-weight: 700; font-size: 46px; }
  .blend-band__weight {
    position: absolute; right: 26px; bottom: 10px;
    color: var(--paper); font-weight: 500; font-size: 20px; text-transform: none;
  }

  .bean-field {
    position: absolute; top: 392px; left: 0; width: 100%; height: 168px;
    background: linear-gradient(160deg, var(--bean-light), var(--bean-dark));
  }

  .roast {
    position: absolute; top: 410px; left: 0; width: 100%;
    display: flex; flex-direction: column; align-items: center; gap: 8px;
  }
  .roast__scale { display: flex; gap: 6px; }
  .roast__dot { width: 11px; height: 11px; border-radius: 50%; background: var(--ember); }
  .roast__dot--off { background: var(--ink); }
  .label--dark .roast__dot--off { background: #4d6366; }
  .roast__level {
    font-family: "Playfair Display SC", serif; font-size: 15px; letter-spacing: 1px;
  }
  .roast__notes { font-size: 14px; font-weight: 400; }
  .label--light .roast__level, .label--light .roast__notes { color: var(--ink); }
  .label--dark .roast__level, .label--dark .roast__notes { color: var(--paper); }
</style>
</head>
<body>
<main class="label-set">

  <section class="label label--light">
    <div class="brand"><span class="brand__dot"></span><span class="brand__name">Pine Ember Coffee</span></div>
    <div class="treeline" role="img" aria-label="Silhouette of pine forest with a campsite tent"></div>
    <div class="blend-band">
      <div class="blend-band__origin">Colombia</div>
      <div class="blend-band__headline">Fair Trade</div>
      <div class="blend-band__sub">Organic Coffee</div>
      <div class="blend-band__weight">450g</div>
    </div>
    <div class="bean-field" role="img" aria-label="Pattern of illustrated coffee beans"></div>
    <div class="roast">
      <div class="roast__scale">
        <span class="roast__dot"></span><span class="roast__dot"></span><span class="roast__dot"></span><span class="roast__dot"></span><span class="roast__dot roast__dot--off"></span>
      </div>
      <div class="roast__level">Medium Dark</div>
      <div class="roast__notes">Toasty Sweet with Dried Red Fruit</div>
    </div>
  </section>

  <section class="label label--dark">
    <div class="brand"><span class="brand__dot"></span><span class="brand__name">Pine Ember Coffee</span></div>
    <div class="treeline" role="img" aria-label="Silhouette of pine forest with a campsite tent"></div>
    <div class="blend-band">
      <div class="blend-band__origin">Colombia</div>
      <div class="blend-band__headline">Fair Trade</div>
      <div class="blend-band__sub">Organic Coffee</div>
      <div class="blend-band__weight">450g</div>
    </div>
    <div class="roast">
      <div class="roast__scale">
        <span class="roast__dot"></span><span class="roast__dot"></span><span class="roast__dot"></span><span class="roast__dot"></span><span class="roast__dot roast__dot--off"></span>
      </div>
      <div class="roast__level">Medium Dark</div>
      <div class="roast__notes">Toasty Sweet with Dried Red Fruit</div>
    </div>
  </section>

</main>
</body>
</html>
```